11 x 11 Flyer Design for Social Media - Reverse Mortgages

62 or older?

A Reverse Mortgage
could be
Your Road to Financial Freedom

* No Monthly Payments
* No Income Requirements
* No Credit Score Requirements
* No Loss of Ownership

Receive cash by lump sum, monthly installments or a line of credit!!

Call us today for a Free Consultation!!
(800) 471-2965

Bluegate Financial Services, Inc.
NMLS #318760
www.bluegatehome.com

```html
<!DOCTYPE html>
<html lang="en">
<head>
<meta charset="utf-8">
<title>Reverse Mortgage Flyer – Bluegate Financial Services</title>
<link href="https://fonts.googleapis.com/css2?family=Roboto:wght@400;500;700&family=Source+Serif+4:ital,wght@1,400;1,600&display=swap" rel="stylesheet">
<style>
  :root {
    --gold: #bca93b;
    --blue: #0c5e8a;
    --blue-deep: #0b5a86;
    --ink: #111111;
    --tick: #8cc63f;
    --white: #ffffff;
  }
  html, body { margin: 0; padding: 0; overflow: hidden; background: var(--white); }
  .flyer {
    position: relative; width: 1200px; height: 1200px; overflow: hidden;
    background: var(--white); font-family: "Roboto", Arial, sans-serif;
  }
  .flyer > * { position: absolute; margin: 0; line-height: 1; }

  .age-question {
    left: 81px; top: 82px; font-family: "Source Serif 4", Georgia, serif;
    font-style: italic; font-weight: 600; font-size: 82px; color: var(--gold);
    letter-spacing: -1px;
  }
  .lead-in { left: 81px; top: 175px; font-size: 50px; font-weight: 400; color: var(--blue); }
  .headline { left: 81px; top: 237px; font-size: 63px; font-weight: 700; color: var(--blue); letter-spacing: -0.5px; }

  .brand {
    left: 916px; top: 34px; width: 252px; height: 149px;
    display: flex; align-items: center; justify-content: center; gap: 10px;
  }
  .brand-dot { width: 22px; height: 22px; border-radius: 50%; background: var(--blue); flex: none; }
  .brand-name { font-size: 19px; font-weight: 700; color: var(--blue); line-height: 1.2; }

  .photo { display: block; }
  .photo-woman-phone { left: 0; top: 329px; width: 397px; height: 306px;
    background: linear-gradient(135deg, #e9ddd6 0%, #a9724f 45%, #8e2a33 100%); }
  .photo-thoughtful-man { left: 397px; top: 329px; width: 403px; height: 306px;
    background: linear-gradient(135deg, #b7dcd3 0%, #8cc3bd 40%, #6a4a3a 75%, #d9e4ef 100%); }
  .photo-couple-selfie { left: 800px; top: 329px; width: 400px; height: 306px;
    background: linear-gradient(135deg, #8fb3d3 0%, #c9b6a8 40%, #5a3a2c 70%, #1d2434 100%); }
  .photo-couple-beach { left: 800px; top: 635px; width: 400px; height: 321px;
    background: linear-gradient(160deg, #c9d4dc 0%, #e8e4df 45%, #6b4634 70%, #f3f3f3 100%); }

  .cash-badge {
    left: 655px; top: 600px; width: 292px; height: 292px; border-radius: 50%;
    background: var(--gold); text-align: center; color: var(--white);
  }
  .cash-badge .pounds { margin-top: 38px; font-size: 54px; font-weight: 700; color: var(--blue-deep); letter-spacing: 2px; }
  .cash-badge .cash-text { margin: 10px auto 0; width: 250px; font-size: 27px; font-weight: 500; line-height: 1.4; letter-spacing: -0.5px; }

  .benefits { left: 81px; top: 672px; list-style: none; padding: 0; }
  .benefits li { display: flex; align-items: center; height: 61px; font-size: 36px; color: var(--ink); }
  .benefits svg { width: 56px; height: 56px; margin-right: 15px; flex: none; }

  .contact-band { left: 0; top: 956px; width: 1200px; height: 244px; background: var(--blue); }
  .call-line {
    left: 81px; top: 983px; font-family: "Source Serif 4", Georgia, serif;
    font-style: italic; font-size: 46px; color: var(--white);
  }
  .consult { left: 81px; top: 1040px; font-size: 62px; font-weight: 700; color: var(--white); letter-spacing: -0.5px; }
  .phone { left: 586px; top: 1032px; font-size: 72px; font-weight: 700; color: var(--gold); letter-spacing: 0.5px; }
  .legal { left: 81px; top: 1148px; font-size: 19px; color: var(--white); }
  .website { right: 79px; top: 1138px; font-size: 34px; font-weight: 700; color: var(--white); }
</style>
</head>
<body>
<main class="flyer">
  <p class="age-question">62 or older?</p>
  <p class="lead-in">A Reverse Mortgage could be</p>
  <h1 class="headline">Your Road to Financial Freedom</h1>

  <div class="brand">
    <span class="brand-dot"></span>
    <span class="brand-name">Bluegate Financial<br>Services, Inc.</span>
  </div>

  <div class="photo photo-woman-phone" role="img" aria-label="Senior woman looking at her mobile phone"></div>
  <div class="photo photo-thoughtful-man" role="img" aria-label="Elderly man deep in thought"></div>
  <div class="photo photo-couple-selfie" role="img" aria-label="Smiling senior couple taking a selfie by the sea"></div>
  <div class="photo photo-couple-beach" role="img" aria-label="Happy senior couple in white on the beach"></div>

  <div class="cash-badge">
    <div class="pounds">£££</div>
    <div class="cash-text">Receive cash by lump sum, monthly installments or a line of credit!</div>
  </div>

  <ul class="benefits">
    <li><svg viewBox="0 0 56 56" aria-hidden="true"><circle cx="24" cy="30" r="24" fill="#0c5e8a"/><path d="M12 30 L22 42 L54 4" fill="none" stroke="#8cc63f" stroke-width="6" stroke-linecap="round" stroke-linejoin="round"/></svg>No Monthly Payments</li>
    <li><svg viewBox="0 0 56 56" aria-hidden="true"><circle cx="24" cy="30" r="24" fill="#0c5e8a"/><path d="M12 30 L22 42 L54 4" fill="none" stroke="#8cc63f" stroke-width="6" stroke-linecap="round" stroke-linejoin="round"/></svg>No Income Requirements</li>
    <li><svg viewBox="0 0 56 56" aria-hidden="true"><circle cx="24" cy="30" r="24" fill="#0c5e8a"/><path d="M12 30 L22 42 L54 4" fill="none" stroke="#8cc63f" stroke-width="6" stroke-linecap="round" stroke-linejoin="round"/></svg>No Credit Score Requirements</li>
    <li><svg viewBox="0 0 56 56" aria-hidden="true"><circle cx="24" cy="30" r="24" fill="#0c5e8a"/><path d="M12 30 L22 42 L54 4" fill="none" stroke="#8cc63f" stroke-width="6" stroke-linecap="round" stroke-linejoin="round"/></svg>No Loss of Ownership</li>
  </ul>

  <div class="contact-band"></div>
  <p class="call-line">Call us today for a</p>
  <p class="consult">Free Consultation</p>
  <p class="phone">(800) 471-2965</p>
  <p class="legal">Bluegate Financial Services, Inc. | &nbsp;NMLS #318760</p>
  <p class="website">www.bluegatehome.com</p>
</main>
</body>
</html>
```